VFX Company Business Card Design Project

The Ember Vale is a decentralized Visual Effects Studio servicing the television and feature film industries.
Project Brief:
Take our logo that was previously designed on Pixel Harbor and make a double sided business card.
Requirements:
- Card MUST be double sided.
- Front of card MUST have the yellow part of our logo against the dark grey background.
- Back of card is completely up to the designer.
- Back of card must include the complete company logo.
Please follow these File Preparation guidelines:
http://printmoor.example/infopage?file=filetype_en&s=PrintMoor_new&lang=en
Industry/Entity Type
Business
Look and feel
Each slider illustrates characteristics of the customer's brand and the style your logo design should communicate.

```html
<!DOCTYPE html>
<html lang="en">
<head>
<meta charset="utf-8">
<title>The Ember Vale – Business Card</title>
<link rel="stylesheet" href="https://fonts.googleapis.com/css2?family=Quicksand:wght@300;400;500;600&display=swap">
<style>
  :root {
    --page: #ffffff;
    --front-bg: #262626;
    --brand-yellow: #fdc823;
    --back-light: #f1f1f4;
    --back-edge: #cdcdd2;
    --ink: #3a3a3c;
    --label-ink: #1e1e1e;
  }
  * { margin: 0; padding: 0; box-sizing: border-box; }
  html, body {
    width: 1200px;
    height: 1000px;
    overflow: hidden;
    background: var(--page);
    font-family: "Quicksand", sans-serif;
  }
  .sheet { position: relative; width: 1200px; height: 1000px; }

  .card { position: absolute; left: 63px; }

  .card--front {
    top: 42px;
    width: 770px;
    height: 452px;
    background: var(--front-bg);
    display: flex;
    align-items: center;
    justify-content: center;
  }
  .card--back {
    top: 511px;
    width: 767px;
    height: 449px;
    background: radial-gradient(ellipse at 50% 42%, var(--back-light) 0%, #e3e3e7 45%, var(--back-edge) 100%);
  }

  .brand {
    display: flex;
    align-items: center;
    gap: 18px;
    color: var(--brand-yellow);
    font-weight: 600;
    white-space: nowrap;
  }
  .brand__dot {
    border-radius: 50%;
    background: var(--brand-yellow);
    flex: none;
  }
  .brand--front { font-size: 64px; margin-top: -38px; }
  .brand--front .brand__dot { width: 56px; height: 56px; }

  .brand--back {
    position: absolute;
    top: 80px;
    left: 0;
    width: 100%;
    justify-content: center;
    font-size: 46px;
    gap: 14px;
  }
  .brand--back .brand__dot { width: 40px; height: 40px; }

  .contact {
    position: absolute;
    left: 0;
    width: 100%;
    color: var(--ink);
    text-align: center;
  }
  .contact__name { top: 183px; font-size: 19px; font-weight: 500; letter-spacing: 0.5px; }
  .contact__role { top: 210px; font-size: 19px; font-weight: 500; letter-spacing: 0.5px; }
  .contact__lines {
    top: 248px;
    left: 368px;
    width: auto;
    text-align: left;
    font-size: 14px;
    line-height: 17.6px;
    font-weight: 500;
    list-style: none;
  }
  .contact__address { top: 342px; left: -2px; font-size: 14px; font-weight: 500; }
  .contact__web { top: 368px; left: -2px; font-size: 14px; font-weight: 500; }

  .side-label {
    position: absolute;
    font-weight: 300;
    font-size: 68px;
    color: var(--label-ink);
    letter-spacing: 2px;
    line-height: 1;
  }
  .side-label--front { left: 856px; top: 370px; }
  .side-label--back { left: 849px; top: 828px; }
</style>
</head>
<body>
<main class="sheet">
  <section class="card card--front" aria-label="Card front">
    <div class="brand brand--front">
      <span class="brand__dot"></span>
      <span class="brand__name">The Ember Vale</span>
    </div>
  </section>

  <section class="card card--back" aria-label="Card back">
    <div class="brand brand--back">
      <span class="brand__dot"></span>
      <span class="brand__name">The Ember Vale</span>
    </div>
    <p class="contact contact__name">Name</p>
    <p class="contact contact__role">Designation</p>
    <ul class="contact contact__lines">
      <li>Email</li>
      <li>Phone</li>
      <li>Mobile</li>
      <li>Fax</li>
    </ul>
    <p class="contact contact__address">Company Address</p>
    <p class="contact contact__web">Website</p>
  </section>

  <p class="side-label side-label--front">Front</p>
  <p class="side-label side-label--back">Back</p>
</main>
</body>
</html>
```